Ridgeway Insulcoat Works Spray Foam Appications website

We need a custom website for our company, www.ridgewayinsulcoatworks.example. We need something we can modify by adding/changing content, photos, updated projects, etc. We are a commercial contractor specializing in Spray Foam applications. We want the website to be very creative and easy to navigate. The main points of the website are to showcase our projects, and describe our scope of services. We provide spray foam applications to the residential and commercial market. We offer Spray Foam roofing applications, as well as Spray Foam interior insulation applications. We also provide Roof Restoration Coating Systems to refurbish old and failing metal roofs. We would be ok with a one page web design if we can get the scope of our services to flow in a single page. The designer can decide if single or multiple pages works best for our business. One of the suppliers we work with is www.vantrexo.example.

Target Market(s)

Residential Home Builders, General Contractors, Commercial Construction Companies, Property Management Groups.

Industry/Entity Type

Insulation

Number of Pages Required

5+ page

Font styles to use
Serif
Sans Serif

Colors

Designer to choose colors to be used in the design.

Requirements
Must have
• We already have a Wix page, so website must be a Wix theme design. Nice easy to navigate format. Color matched to our current logo theme. We already have brochures and would like for it to match what's already in the hands of some of our customers. Need to be able to manage content to update photos, projects, scope of service, etc., via Wix. Current hold/splash page is hosted at www.ridgewayinsulcoatworks.example. We would also like to have this video posted on the home page: https://www.videohost.example/watch?v=QzT4kLp9wXe&feature=share
Nice to have
• I have attached some splash videos, being able to incorporate these somehow without being overpowering would be nice.

```html
<!DOCTYPE html>
<html lang="en">
<head>
<meta charset="utf-8">
<title>Ridgeway Insulcoat Works</title>
<link href="https://fonts.googleapis.com/css2?family=Open+Sans:ital,wght@0,400;0,600;1,400&display=swap" rel="stylesheet">
<style>
:root{
  --sidebar:#232323;
  --footer:#242424;
  --hero-gray:#e6e6e6;
  --band:#f1f1f1;
  --orange:#f5a623;
  --ink:#1b1b1b;
  --text:#333;
  --muted:#8a8a8a;
  --icon:#6b6b6b;
}
*{margin:0;padding:0;box-sizing:border-box}
html,body{width:1200px;height:3341px;overflow:hidden;background:#fff}
body{position:relative;font-family:"Open Sans",Arial,sans-serif;color:var(--text)}
.abs{position:absolute}
.sidebar{left:0;top:0;width:80px;height:3341px;background:var(--sidebar)}
.side-mark{left:16px;top:42px;width:48px;height:48px;border:3px solid var(--orange);border-radius:50%}
.burger{left:30px;top:533px;width:21px}
.burger span{display:block;height:3px;background:#fff;margin-bottom:5px}
.hero-media{left:80px;top:0;width:520px;height:614px;background:linear-gradient(110deg,#4a3a2a 0%,#7a6348 35%,#8d8fa8 55%,#b9a3a6 70%,#5e4a36 100%)}
.play{left:316px;top:284px}
.hero-side{left:600px;top:0;width:600px;height:614px;background:var(--hero-gray)}
.social{left:1119px;width:16px;height:16px;border-radius:50%;background:var(--icon)}
.brand{left:680px;top:250px;display:flex;align-items:center;gap:16px}
.brand-dot{width:112px;height:112px;border:6px solid var(--orange);border-radius:50%}
.brand-name{font-size:30px;font-weight:600;color:var(--orange);line-height:1.15;width:260px}
.chat{left:1096px;top:511px;width:64px;height:64px;border-radius:50%;background:var(--orange);display:flex;align-items:center;justify-content:center}
.intro{left:264px;top:686px;width:672px;text-align:center;font-size:16.5px;line-height:32px;color:#333}
.contact{left:80px;top:880px;width:1040px;text-align:center;font-size:16.5px;color:#222}
.contact i{font-style:normal;margin:0 22px}
.rule{left:198px;width:803px;height:1px;background:var(--orange)}
.svc-img{width:496px;height:319px}
.ring{width:132px;height:132px;border:6px solid var(--orange);border-radius:50%}
.svc-title{font-size:34px;line-height:40px;color:var(--ink);font-weight:400}
.svc-text{font-size:11.5px;line-height:21px;color:#333;width:370px}
.more{font-size:10.5px;font-style:italic;color:#222}
.more b{font-style:normal;font-weight:600;margin-left:6px}
.section-title{left:80px;width:1120px;text-align:center;font-size:34px;color:var(--ink)}
.quote{left:270px;top:2472px;width:660px;text-align:center;font-size:16.5px;line-height:32px}
.author{left:80px;top:2582px;width:1120px;text-align:center;font-size:16px;font-weight:600;line-height:26px;color:#222}
.arrow{top:2506px}
.band{left:80px;top:2702px;width:1120px;height:359px;background:var(--band)}
.thumb{top:2830px;width:160px;height:160px}
.footer{left:80px;top:3061px;width:1120px;height:280px;background:var(--footer)}
.join{left:144px;top:3108px;font-size:25px;font-weight:600;color:var(--orange)}
.email{left:144px;top:3180px;width:360px;border-bottom:1px solid #bbb;padding:0 14px 10px;font-size:16px;color:#8e8e8e}
.subscribe{left:144px;top:3236px;width:360px;height:47px;background:var(--orange);color:#111;font-size:15px;font-weight:600;text-align:center;line-height:47px}
.f-info{left:685px;top:3110px;font-size:16px;line-height:32px;color:var(--muted)}
.f-rule{left:685px;top:3219px;width:370px;height:1px;background:#444}
.copy{left:685px;top:3238px;font-size:16px;line-height:25px;color:var(--muted)}
</style>
</head>
<body>
<div class="abs sidebar"></div>
<div class="abs side-mark"></div>
<div class="abs burger"><span></span><span></span><span></span></div>

<div class="abs hero-media" role="img" aria-label="Video still: spray foam being applied around a window frame"></div>
<svg class="abs play" width="48" height="48" viewBox="0 0 48 48"><circle cx="24" cy="24" r="24" fill="#fff"/><path d="M19 14l14 10-14 10z" fill="#111"/></svg>
<div class="abs hero-side"></div>
<div class="abs social" style="top:43px"></div>
<div class="abs social" style="top:94px"></div>
<div class="abs social" style="top:145px"></div>
<div class="abs social" style="top:196px"></div>
<div class="abs brand"><div class="brand-dot"></div><div class="brand-name">Ridgeway Insulcoat Works</div></div>
<div class="abs chat"><svg width="26" height="22" viewBox="0 0 26 22"><ellipse cx="13" cy="10" rx="12" ry="8.5" fill="#111"/><path d="M5 15l-3 6 8-4z" fill="#111"/></svg></div>

<p class="abs intro">Nullam accumsan purus vel tempus viverra. Mauris suscipit felis id nunc elementum varius. Praesent elementum nulla sit amet justo pellentesque scelerisque. Nam et tortor in ante iaculis porttitor in luctus mi. Vivamus gravida sem a pretium euismod. Nam lob-ortis, purus et fringilla tempus, risus eros dignissim diam, eget finibus sem risus sit amet eros. Vestibulum facilisis dolor at purus tincidunt porta.</p>
<p class="abs contact">24 Building name, Street name, City Zipcode<i>|</i>1-555-014-3380<i>|</i>info@ridgewayinsulcoatworks.example</p>
<div class="abs rule" style="top:927px"></div>

<div class="abs svc-img" style="left:144px;top:1008px;background:linear-gradient(180deg,#7d8184 0%,#e9e4cf 30%,#d8d2bc 62%,#7c7b78 75%,#b3b3b3 100%)" role="img" aria-label="Warehouse walls covered in sprayed foam insulation"></div>
<div class="abs ring" style="left:598px;top:1000px"></div>
<h2 class="abs svc-title" style="left:692px;top:1052px">Spray Foam interior<br>insulation applications</h2>
<p class="abs svc-text" style="left:692px;top:1153px">Aenean aliquet risus metus, vitae tristique enim finibus eu. Sed iaculis nisl est, vitae sagittis risus fermentum sed. Donec lobortis, dui sed eleifend pellentesque, erat dui tincidunt urna,</p>
<p class="abs more" style="left:692px;top:1231px">Read More<b>›</b></p>

<h2 class="abs svc-title" style="left:144px;top:1500px">Roofing Applications</h2>
<p class="abs svc-text" style="left:144px;top:1558px">Aenean aliquet risus metus, vitae tristique enim finibus eu. Sed iaculis nisl est, vitae sagittis risus fermentum sed. Donec lobortis, dui sed eleifend pellentesque, erat dui tincidunt urna,</p>
<p class="abs more" style="left:144px;top:1636px">Read More<b>›</b></p>
<div class="abs svc-img" style="left:559px;top:1456px;background:linear-gradient(180deg,#5d6670 0%,#8a8b80 22%,#c9cbcc 40%,#e6e7e8 70%,#c7c8ca 100%)" role="img" aria-label="Worker on a foam-coated commercial roof"></div>
<div class="abs ring" style="left:466px;top:1448px"></div>

<div class="abs svc-img" style="left:144px;top:1904px;background:linear-gradient(180deg,#6f8fbf 0%,#9db4d4 14%,#3f4a3c 20%,#9ea1a3 30%,#dcdcdc 60%,#b9b9b9 100%)" role="img" aria-label="Restored metal roof with white coating"></div>
<div class="abs ring" style="left:598px;top:1895px"></div>
<h2 class="abs svc-title" style="left:692px;top:1948px">Roof Restoration<br>Coating Systems</h2>
<p class="abs svc-text" style="left:692px;top:2048px">Aenean aliquet risus metus, vitae tristique enim finibus eu. Sed iaculis nisl est, vitae sagittis risus fermentum sed. Donec lobortis, dui sed eleifend pellentesque, erat dui tincidunt urna,</p>
<p class="abs more" style="left:692px;top:2126px">Read More<b>›</b></p>

<div class="abs rule" style="top:2335px"></div>
<h2 class="abs section-title" style="top:2404px">Testimonials</h2>
<svg class="abs arrow" style="left:144px" width="16" height="28" viewBox="0 0 16 28"><path d="M13 2L3 14l10 12" fill="none" stroke="#333" stroke-width="3"/></svg>
<p class="abs quote">“ Sed elementum odio nunc, gravida mattis lorem interdum tempor. Etiam consequat lacus a felis viverra, eget rhoncus massa ullamcorper. Sed quis tincidunt neque. Mauris tellus metus, commodo at quam et, fringilla ullamcorper nisl. “</p>
<svg class="abs arrow" style="left:1040px" width="16" height="28" viewBox="0 0 16 28"><path d="M3 2l10 12L3 26" fill="none" stroke="#333" stroke-width="3"/></svg>
<p class="abs author">Mara Venn,<br>City</p>

<div class="abs band"></div>
<h2 class="abs section-title" style="top:2762px">Projects</h2>
<div class="abs thumb" style="left:105px;background:linear-gradient(180deg,#3f6aa8 0%,#c9b58a 30%,#e2cf80 60%,#b9a66a 100%)" role="img" aria-label="Project: foam roof on industrial building"></div>
<div class="abs thumb" style="left:287px;background:linear-gradient(180deg,#3a5f98 0%,#7a98c2 40%,#d4d8de 55%,#586070 100%)" role="img" aria-label="Project: coated standing-seam roof"></div>
<div class="abs thumb" style="left:469px;background:linear-gradient(180deg,#8fa2bd 0%,#5a5e58 30%,#e5e6e7 55%,#c8c9cb 100%)" role="img" aria-label="Project: white coated roof"></div>
<div class="abs thumb" style="left:651px;background:linear-gradient(135deg,#4b4a40 0%,#d7cf9f 40%,#8d8766 70%,#2e2e2a 100%)" role="img" aria-label="Project: close view of ribbed metal roof"></div>
<div class="abs thumb" style="left:833px;background:linear-gradient(180deg,#4775b3 0%,#4e5a4c 25%,#d9cd8e 55%,#bfb07a 100%)" role="img" aria-label="Project: foam roof in progress"></div>
<div class="abs thumb" style="left:1015px;background:linear-gradient(180deg,#5e82b8 0%,#8a8c88 30%,#ecedee 60%,#cfd0d2 100%)" role="img" aria-label="Project: finished roof coating"></div>

<div class="abs footer"></div>
<h3 class="abs join">Join Our Mailing List</h3>
<div class="abs email">Enter your email here*</div>
<div class="abs subscribe">SUBSCRIBE HERE</div>
<p class="abs f-info">24 Building name, Street name,City Zipcode<br>1-555-014-3380<br>info@ridgewayinsulcoatworks.example</p>
<div class="abs f-rule"></div>
<p class="abs copy">Copyright &nbsp;©&nbsp; 2020 &nbsp; Ridgeway Insulcoat Works, LLC.<br>Alll rights reserved.</p>
</body>
</html>
```